ALL TEXT GRAPHICS TM May 2025 for Instagram

We are looking for a series of social media graphics for Instagram (new size: 4:5 (1080 x 1350 pixels) ratio that are ALL TEXT. We want the following quotes below on each graphic; one quote per graphic. AND, In very small letters at the bottom of each graphic, add @TovaMarshOnline
The look and feel of these graphics should be complimentary to the color palette attached below; but keep them simple. But the design is up to you; at the end of this document, I provided various samples of all text graphics that I like as examples.
Target Market(s)
women looking to lose weight
Look and feel

```html
<!DOCTYPE html>
<html lang="en">
<head>
<meta charset="utf-8">
<title>Hormones – Tova Marsh</title>
<link rel="stylesheet" href="https://fonts.googleapis.com/css2?family=EB+Garamond:wght@400;500&family=Poppins:wght@600&display=swap">
<style>
  :root {
    --paper: #ffffff;
    --ink: #111111;
    --accent: #ff3aa0;
    --on-accent: #ffffff;
  }
  html, body {
    margin: 0;
    padding: 0;
    width: 960px;
    height: 1200px;
    overflow: hidden;
    background: var(--paper);
  }
  .post {
    position: relative;
    width: 960px;
    height: 1200px;
    background: var(--paper);
    font-family: "EB Garamond", Garamond, serif;
    color: var(--ink);
  }
  .bracket {
    position: absolute;
    left: 0;
    top: 0;
  }
  .line {
    position: absolute;
    left: 89px;
    margin: 0;
    font-size: 71px;
    line-height: 1;
    font-weight: 400;
    white-space: nowrap;
  }
  .headline-1 { top: 259px; }
  .headline-2 { top: 345px; }
  .headline-3 { top: 431px; }
  .cta-lead   { top: 628px; left: 86px; }
  .cta-tail   { top: 879px; }
  .keyword-band {
    position: absolute;
    left: 90px;
    top: 723px;
    width: 795px;
    height: 133px;
    background: var(--accent);
  }
  .keyword {
    position: absolute;
    left: 41px;
    top: 17px;
    margin: 0;
    font-size: 96px;
    line-height: 1;
    font-weight: 400;
    color: var(--on-accent);
    letter-spacing: 0.5px;
  }
  .handle {
    position: absolute;
    left: 0;
    right: 0;
    top: 1135px;
    text-align: center;
    font-family: "Poppins", Arial, sans-serif;
    font-weight: 600;
    font-size: 33px;
    line-height: 1;
    color: var(--accent);
  }
</style>
</head>
<body>
<main class="post">
  <svg class="bracket" width="960" height="600" viewBox="0 0 960 600" aria-hidden="true">
    <path d="M418 205 H87 A35 35 0 0 0 52 240 V527" fill="none" stroke="var(--accent)" stroke-width="4"/>
    <polygon points="418,180 449,205 418,230 387,205" fill="var(--accent)"/>
    <polygon points="52,496 78,527 52,558 26,527" fill="var(--accent)"/>
  </svg>

  <p class="line headline-1">Your belly isn’t fat…</p>
  <p class="line headline-2">it’s hormonal.</p>
  <p class="line headline-3">And here’s how to fix it.</p>

  <p class="line cta-lead">comment</p>
  <div class="keyword-band">
    <p class="keyword">HORMONES</p>
  </div>
  <p class="line cta-tail">if nothing is working.</p>

  <div class="handle">@TovaMarshOnline</div>
</main>
</body>
</html>
```